Wordpress Design Project for Bankruptcy Law Office in San Francisco

our current website: www.dorvanetzlaw.example

we would like to re-design it for wordpress to make it faster and a bit more modern.

content should be similar to what we have there right now but also we do family law

please include logo for law office:

Law Office of Marta K. Zelobrodna

Thank you.
Updates

please see attached word document with logos that we like as an example.

we do tend to like color red.  darker red.

Please submit your design variations and logo as soon as possible.   We would like to go over them and make our decision

Reason: Please create couple of more variations of logo for your design, so we can make our decision what we like the most. Please see word doc for samples: Text: Law Office Of Marta K. Zelobrodna

Reason: final touches

Target Market(s)

bankruptcy and family law clients

Industry/Entity Type

Family Law

Requirements
Must have
• see examples of law sites
http://outreach.lexorvin.example/testimonials

- new logo: Law Office of Marta K. Zelobrodna
- client intake form
- blog
- contact us form

Nice to have
• - map
- red color
- on the front page a nice photo of SF or a happy family

```html
<!DOCTYPE html>
<html lang="en">
<head>
<meta charset="utf-8">
<title>Law Office of Marta K. Zelobrodna</title>
<link href="https://fonts.googleapis.com/css2?family=Bitter:wght@700&family=Lato:wght@400;700&display=swap" rel="stylesheet">
<style>
:root{
  --red:#c0141a;
  --red-dark:#8f0e12;
  --btn-red:#d71a1f;
  --charcoal:#444342;
  --charcoal-dark:#3a3938;
  --page-bg:#f1eeea;
  --panel:#f5f1ee;
  --panel-head:#e8e1dd;
  --text:#6f6a66;
  --heading:#4a4643;
  --white:#ffffff;
}
*{margin:0;padding:0;box-sizing:border-box}
html,body{width:778px;height:1200px;overflow:hidden}
body{position:relative;background:var(--page-bg);font-family:'Lato',sans-serif;color:var(--text)}
.top-band{position:absolute;left:0;top:0;width:778px;height:130px;background:var(--charcoal)}
.call-us{position:absolute;right:78px;top:23px;color:#ddd;font-size:13px;letter-spacing:.3px}
.call-us strong{color:#fff;font-weight:700}
.page{position:absolute;left:78px;top:45px;width:622px;height:1122px;background:var(--white)}
.abs{position:absolute}
.header{left:84px;top:52px;width:610px;height:78px;background:var(--red)}
.logo-small{left:15px;top:33px;color:#fff;font-family:'Bitter',serif;font-size:9px;font-weight:700}
.logo-name{left:15px;top:44px;color:#fff;font-family:'Bitter',serif;font-size:21px;font-weight:700;white-space:nowrap}
.nav{left:265px;top:0;height:78px;display:flex;font-size:9.5px;color:#fff;text-transform:uppercase}
.nav span{padding:0 6px;line-height:117px;height:78px}
.nav .active{background:var(--red-dark)}
.dropdown{left:487px;top:130px;width:115px;height:58px;background:var(--charcoal-dark);font-size:7.5px;color:#ccc;text-transform:uppercase}
.dropdown div{padding:0 6px;height:24px;line-height:24px;border-bottom:1px solid #555;margin:3px 0}
.dropdown div:last-child{border:none}
.hero{left:84px;top:137px;width:610px;height:226px;background:#f5f2ec}
.hero-photo{left:0;top:0;width:305px;height:226px;background:linear-gradient(90deg,#6a5340 0%,#c9b8a2 40%,#ece3d6 75%,#f5f2ec 100%)}
.hero-kicker{left:303px;top:37px;color:var(--red);font-size:11.5px}
.hero-title{left:303px;top:48px;color:var(--red);font-size:24px;font-weight:400;white-space:nowrap}
.hero-text{left:303px;top:86px;width:290px;font-size:8.6px;line-height:15.6px;color:#4e4a46}
.newsletter{left:304px;top:160px;width:293px;height:54px;background:var(--charcoal);border:1px solid #222}
.newsletter h3{position:absolute;left:10px;top:7px;color:#fff;font-size:12px;font-weight:400}
.newsletter .field{position:absolute;left:7px;top:27px;width:221px;height:19px;background:#fff;border:1px solid #bbb;font-size:8.5px;color:#aaa;padding:3px 6px}
.newsletter .btn{position:absolute;left:234px;top:27px;width:52px;height:19px;background:var(--btn-red);border:1px solid #7a0c0f;color:#fff;font-size:8.5px;text-align:center;line-height:17px}
.intro{left:84px;top:370px;width:610px;height:154px;background:var(--panel)}
.intro-col{top:14px;width:272px}
.intro-col h2{font-size:13px;font-weight:400;color:var(--heading);padding-bottom:5px;border-bottom:1px solid var(--red);margin-bottom:7px}
.intro-col p{font-size:8.6px;line-height:15.6px}
.card{top:532px;width:194px;height:259px;background:var(--panel)}
.card h2,.box h2{height:32px;line-height:34px;padding-left:12px;background:var(--panel-head);font-size:12.5px;font-weight:400;color:var(--heading)}
.card-img{position:absolute;left:13px;top:45px;width:168px;height:77px}
.card p{position:absolute;left:13px;top:134px;width:170px;font-size:8.6px;line-height:14.4px}
.btn-red{position:absolute;background:var(--btn-red);color:#fff;text-transform:uppercase;font-size:7.5px;text-align:center}
.card .btn-red{left:110px;top:228px;width:71px;height:18px;line-height:18px}
.box{top:798px;height:291px;background:var(--panel)}
.post{position:absolute;left:13px;width:272px;border-bottom:1px solid #e0d8d3;height:79px}
.post .date{font-size:6.5px;color:var(--red);text-transform:uppercase}
.post h3{font-size:9.5px;font-weight:700;color:#3e3a37;margin:3px 0 7px}
.post p{font-size:8.3px;line-height:11.8px;width:262px}
.input{position:absolute;left:13px;width:175px;height:18px;background:#fff;border:1px solid #ddd;font-size:8px;color:#aaa;font-style:italic;padding:3px 7px}
.textarea{position:absolute;left:13px;top:181px;width:273px;height:70px;background:#fff;border:1px solid #ddd}
.footer{left:84px;top:1096px;width:610px;height:65px;background:var(--charcoal);color:#fff;text-align:center}
.footer .copy{margin-top:13px;font-size:9px}
.footer .legal{margin:6px auto 0;width:530px;font-size:5.3px;line-height:7.8px;color:#ddd}
</style>
</head>
<body>
<div class="top-band"></div>
<div class="call-us">CALL US: <strong>(415) 555-0187</strong></div>
<div class="page"></div>

<header class="abs header">
  <div class="abs logo-small">Law Office Of</div>
  <div class="abs logo-name">Marta K. Zelobrodna</div>
  <nav class="abs nav">
    <span>About</span><span>Areas of Practice</span><span class="active">Resources</span><span>Blog</span><span>FAQ</span><span>Contact</span>
  </nav>
</header>
<div class="abs dropdown"><div>Resources</div><div>Download Forms</div></div>

<section class="abs hero">
  <div class="abs hero-photo" role="img" aria-label="Photo of a bronze Lady Justice statue beside an attorney reading at her desk"></div>
  <div class="abs hero-kicker">Law Offices of</div>
  <h1 class="abs hero-title">Marta K. Zelobrodna</h1>
  <p class="abs hero-text">The Law Offices of Marta K. Zelobrodna is a consumer law office dedicated to consumer protection and zealously defending the rights of our clients. We offer the big firm quality legal representation with a small firm individualized attention to each client.</p>
  <form class="abs newsletter">
    <h3>Subscribe to Newsletter</h3>
    <div class="field">Enter your email</div>
    <div class="btn">Submit</div>
  </form>
</section>

<section class="abs intro">
  <div class="abs intro-col" style="left:13px">
    <h2>Welcome to our Law Office</h2>
    <p>Our office offers services in all types of consumer bankruptcy filings, i.e. Chapter 7, Chapter 13, Chapter 11, negotiating a settlement of your debts, assisting you in the defense of collection litigation and defending you against foreclosure. Please review our site and see what we may be able to offer you. Feel free to call us at (415) 555-0187 or use our free case evaluation form.</p>
  </div>
  <div class="abs intro-col" style="left:325px">
    <h2>Speak to the Lawyer directly</h2>
    <p>Unlike some other law firms, when you call the Law Office of Marta K. Zelobrodna you will speak to an actual attorney. Not a paralegal or assistant. And even after retaining our office you will still speak to an attorney unlike other firms where you cannot get a hold of your attorney after several attempts.</p>
  </div>
</section>

<article class="abs card" style="left:84px">
  <h2>Debt relief</h2>
  <div class="card-img" role="img" aria-label="Photo of index tabs labelled consulting and debts" style="background:linear-gradient(135deg,#d9d2c6,#a89886 60%,#c9a27e)"></div>
  <p>Etiam dignissim ante ac diam pellentesque facilisis! Sed vitae urna nibh. Proin risus sem, viverra ac tincidunt vitae, scelerisque in purus. Nullam scelerisque, quam non porta vehicula, nibh magna scelerisque ipsum, vel pellentesque turpis sem id eros!</p>
  <a class="btn-red">Know more</a>
</article>
<article class="abs card" style="left:292px">
  <h2>Foreclosure Prevention</h2>
  <div class="card-img" role="img" aria-label="Photo of a house with a foreclosure for-sale sign" style="background:linear-gradient(180deg,#7fa6d6,#dfe6ea 45%,#8a9a6a 85%,#c23a2c)"></div>
  <p>Etiam dignissim ante ac diam pellentesque facilisis! Sed vitae urna nibh. Proin risus sem, viverra ac tincidunt vitae, scelerisque in purus. Nullam scelerisque, quam non porta vehicula, nibh magna scelerisque ipsum, vel pellentesque turpis sem id eros!</p>
  <a class="btn-red">Know more</a>
</article>
<article class="abs card" style="left:500px">
  <h2>Chapter 13</h2>
  <div class="card-img" role="img" aria-label="Photo of a bankruptcy worksheet with glasses and a pen" style="background:linear-gradient(135deg,#9c9690,#e6e2dc 50%,#bdb7b0)"></div>
  <p>Etiam dignissim ante ac diam pellentesque facilisis! Sed vitae urna nibh. Proin risus sem, viverra ac tincidunt vitae, scelerisque in purus. Nullam scelerisque, quam non porta vehicula, nibh magna scelerisque ipsum, vel pellentesque turpis sem id eros!</p>
  <a class="btn-red">Know more</a>
</article>

<section class="abs box" style="left:84px;width:298px">
  <h2>From my Blog</h2>
  <div class="post" style="top:45px">
    <div class="date">Sep 03, 2012</div>
    <h3>Etiam felis magna, malesuada quis susc</h3>
    <p>Pellentesque habitant morbi tristique senectus et netus et malesuada fames ac turpis egestas. Etiam felis magna, malesuada quis suscipit ultricies, ullamcorper</p>
  </div>
  <div class="post" style="top:124px">
    <div class="date">Sep 01, 2012</div>
    <h3>Etiam felis magna, malesuada quis susc</h3>
    <p>Pellentesque habitant morbi tristique senectus et netus et malesuada fames ac turpis egestas. Etiam felis magna, malesuada quis suscipit ultricies, ullamcorper</p>
  </div>
  <div class="post" style="top:202px">
    <div class="date">Aug 28, 2012</div>
    <h3>Etiam felis magna, malesuada quis susc</h3>
    <p>Pellentesque habitant morbi tristique senectus et netus et malesuada fames ac turpis egestas. Etiam felis magna, malesuada quis suscipit ultricies, ullamcorper</p>
  </div>
</section>

<section class="abs box" style="left:395px;width:299px">
  <h2>Contact me</h2>
  <div class="input" style="top:52px">Name</div>
  <div class="input" style="top:84px">Email</div>
  <div class="input" style="top:116px">Phone</div>
  <div class="input" style="top:149px">Subject</div>
  <div class="textarea"></div>
  <a class="btn-red" style="left:220px;top:258px;width:65px;height:20px;line-height:20px;font-size:9px;text-transform:none">Submit</a>
</section>

<footer class="abs footer">
  <div class="copy">Copyright © 2010 dorvanetzlaw.example. All Rights Reserved</div>
  <p class="legal">Disclaimer: The Law Offices of Marta K. Zelobrodna is a Debt Relief law firm as defined by 11 U.S.C. 528. We help people file for Bankruptcy Relief under the Bankruptcy Code. The information contained on this website is not to be construed as legal advice. It is not intended to solicit or form an attorney-client relationship. We do not guarantee any result and prior results do not guarantee a similar outcome. This is an attorney advertisement and this website is for informational purposes only.</p>
</footer>
</body>
</html>
```